Poster Design Project

Looking for a poster for my lobby. The poster will be big so it will need to be high resolution. I will attach a photo of the last one I had done, but it is not big enough, and the images are outdated.

```html
<!DOCTYPE html>
<html lang="en">
<head>
<meta charset="utf-8">
<title>We'll loan or pay you cash on</title>
<link href="https://fonts.googleapis.com/css2?family=Alfa+Slab+One&family=Oswald:wght@500;700&display=swap" rel="stylesheet">
<style>
  :root {
    --green-deep: #0f4a1a;
    --green-dark: #17612a;
    --green-light: #1e7533;
    --gold-light: #fbe98a;
    --gold-mid: #e2b64a;
    --gold-dark: #b98424;
    --yellow: #f4df3c;
    --card-border: #f5c518;
    --white: #ffffff;
  }
  * { margin: 0; padding: 0; box-sizing: border-box; }
  html, body { width: 800px; height: 1200px; overflow: hidden; background: var(--green-dark); }
  .poster {
    position: relative; width: 800px; height: 1200px; overflow: hidden;
    background: var(--green-dark);
    font-family: "Oswald", "Arial Narrow", sans-serif;
  }
  .side-band {
    position: absolute; left: 0; top: 0; width: 188px; height: 1200px;
    background: var(--green-deep);
  }
  .gold-strip {
    position: absolute; left: 16px; top: 0; width: 164px; height: 1200px;
    background: linear-gradient(90deg, var(--gold-dark) 0%, var(--gold-light) 35%, var(--gold-mid) 70%, var(--gold-dark) 100%);
  }
  .cash-photo {
    position: absolute; left: 20px; top: 4px; width: 160px; height: 196px;
    background: linear-gradient(160deg, #dfe6d4 0%, #b9c6a8 55%, #8fa07c 100%);
    border-radius: 4px;
  }
  .tagline { position: absolute; left: 40px; top: 190px; width: 130px; height: 1000px; }
  .row { position: absolute; left: 188px; width: 612px; }
  .row.light { background: var(--green-light); }
  .row.dark { background: var(--green-dark); }
  .category {
    position: absolute; right: 372px; text-align: right;
    font-weight: 700; font-size: 44px; line-height: 52px;
    color: var(--yellow); text-shadow: 2px 2px 3px rgba(0,0,0,.45);
    white-space: nowrap;
  }
  .card {
    position: absolute; left: 448px; width: 194px; height: 164px;
    background: linear-gradient(180deg, #ffffff, #eef0ee);
    border: 4px solid var(--card-border); border-radius: 12px;
    transform: skewY(-1.5deg);
    box-shadow: 3px 4px 8px rgba(0,0,0,.45);
    overflow: hidden;
  }
  .card .photo { position: absolute; inset: 10px; border-radius: 6px; }
  .note {
    position: absolute; right: 8px; text-align: right;
    font-weight: 500; font-size: 16px; line-height: 20px; color: var(--white);
    text-shadow: 1px 1px 2px rgba(0,0,0,.5);
  }
  .closing {
    position: absolute; right: 16px; top: 1148px;
    font-family: "Alfa Slab One", Georgia, serif; font-size: 30px; color: var(--white);
    letter-spacing: .5px;
  }
</style>
</head>
<body>
<div class="poster">
  <div class="side-band"></div>
  <div class="gold-strip"></div>
  <div class="cash-photo" role="img" aria-label="Fanned stack of hundred-dollar bills"></div>
  <svg class="tagline" viewBox="0 0 130 1000" aria-label="We'll loan or pay you cash on">
    <text transform="translate(112 990) rotate(-90)" x="0" y="0" textLength="980" lengthAdjust="spacingAndGlyphs"
      font-family="Alfa Slab One, Georgia, serif" font-size="110" fill="#1a5a24" stroke="#f4df3c" stroke-width="4" paint-order="stroke">We'll loan or pay you cash on</text>
  </svg>

  <div class="row light" style="top:0;height:192px"></div>
  <div class="row dark" style="top:192px;height:184px"></div>
  <div class="row light" style="top:376px;height:180px"></div>
  <div class="row dark" style="top:556px;height:180px"></div>
  <div class="row light" style="top:736px;height:192px"></div>
  <div class="row dark" style="top:928px;height:184px"></div>
  <div class="row light" style="top:1112px;height:88px"></div>

  <div class="category" style="top:68px">Jewelry &amp;<br>Collectibles</div>
  <div class="card" style="top:42px"><div class="photo" role="img" aria-label="Gold coin, diamond, ring, gold chain and a wristwatch" style="background:linear-gradient(135deg,#f3ead0,#d9c07a 50%,#5a5a5a)"></div></div>
  <div class="note" style="top:106px">Old &amp; Broken Gold<br>Antique Collectibles<br>Diamonds &amp; Watches</div>

  <div class="category" style="top:244px">Computers<br>&amp; Laptops</div>
  <div class="card" style="top:228px"><div class="photo" role="img" aria-label="Tablet, laptop, camera and smartphone" style="background:linear-gradient(135deg,#e8e8e8,#e0833a 45%,#2a2a2a)"></div></div>
  <div class="note" style="top:308px">Tablets<br>Cameras</div>

  <div class="category" style="top:428px">Power<br>Tolls</div>
  <div class="card" style="top:416px"><div class="photo" role="img" aria-label="Cordless screwdriver and clothes iron" style="background:linear-gradient(135deg,#f0f0f0,#7fc24a 50%,#3a4a3a)"></div></div>
  <div class="note" style="top:464px">Home &amp;<br>Garden Equipment</div>

  <div class="category" style="top:618px">Video Games<br>&amp; Systems</div>
  <div class="card" style="top:600px"><div class="photo" role="img" aria-label="Game console with two controllers" style="background:linear-gradient(135deg,#f4f4f4,#6b7a9a 50%,#151515)"></div></div>

  <div class="category" style="top:814px">Sports<br>Equipment</div>
  <div class="card" style="top:788px"><div class="photo" role="img" aria-label="Treadmill and basketball" style="background:linear-gradient(135deg,#f2f2f2,#9a9a9a 50%,#d9661e)"></div></div>

  <div class="category" style="top:998px">Musical<br>Instruments</div>
  <div class="card" style="top:978px"><div class="photo" role="img" aria-label="Keyboard, electric guitar and snare drum" style="background:linear-gradient(135deg,#f0f0f0,#2a2a2a 50%,#b8431e)"></div></div>

  <div class="closing">And anything else of value ...</div>
</div>
</body>
</html>
```